Orvik Lines website

i'm looking for a promotional website for my business.
we provide Rope Access, Work at Height & Difficult Access services.
we treat water leak into buildings, external renovation of buildings, windows cleaning, confined spaces services and practically jobs in which the access is difficult.
here are examples of web site i like :
http://www.layoutbazaar.example/wordpress-themes/51872.html
http://www.layoutbazaar.example/joomla-templates/51294.html

private people, commercial household chiefs, maintenance managers

Business

• - mobile friendly
- frindlo redirection
- 5 tabs
- one more customizable page - so i can add a photo and a description of the service corresponding (for now i offer 7 different services)
- contact us on each page with no redirection
- we are offering 7 different services
the website will be published in Israel which means right to left or centered for english option in the future. (logo on left hand corner)

- no flash
- should be future customisable - for future
• - a space for a slogan
- non scrollable
- photos on the landing page + redirection to gallery (photos and short films)
- 3 dynamic banners with short description of the theme of each, clicking on the banner after it opened will redirect to it's corresponding page.

```html
<!DOCTYPE html>
<html lang="en">
<head>
<meta charset="utf-8">
<title>Orvik Lines — Rope Access &amp; Work at Height</title>
<link rel="stylesheet" href="https://fonts.googleapis.com/css2?family=Montserrat:wght@300;400;600;700&family=Lato:wght@400;700&display=swap">
<style>
:root{
  --green:#3dd157;
  --green-dark:#27a83d;
  --ink:#1a1a1a;
  --band:#1c1c1c;
  --band-alt:#202020;
  --band-deep:#161616;
  --footer:#0b0b0b;
  --text:#d9d9d9;
  --muted:#9a9a9a;
  --rule:#3a3a3a;
  --header-top:#ffffff;
  --header-bottom:#e4e4e4;
}
*{margin:0;padding:0;box-sizing:border-box}
html,body{width:970px;height:1200px;overflow:hidden;background:var(--band)}
body{position:relative;font-family:"Lato",Arial,sans-serif;color:var(--text)}
.abs{position:absolute}

/* header */
.site-header{position:absolute;left:0;top:0;width:970px;height:69px;
  background:linear-gradient(var(--header-top),var(--header-bottom));border-bottom:2px solid #111}
.brand{position:absolute;left:241px;top:22px;font-family:"Montserrat",sans-serif;font-weight:700;
  font-size:20px;color:var(--ink);display:flex;align-items:center;gap:8px}
.brand-dot{width:14px;height:14px;border-radius:50%;background:var(--ink)}
.main-nav a{position:absolute;top:29px;font-family:"Montserrat",sans-serif;font-weight:600;font-size:10px;
  color:#111;text-decoration:none;letter-spacing:.3px}
.nav-active-bar{position:absolute;left:428px;top:0;width:48px;height:3px;background:#222}

/* hero */
.hero-media{position:absolute;left:0;top:69px;width:970px;height:379px;
  background:radial-gradient(circle at 72% 40%,#5a5a5a 0,#8a8a8a 30%,#4a4a4a 70%,#2e2e2e 100%)}
.hero-lead{left:220px;top:184px;font-family:"Montserrat",sans-serif;font-weight:300;font-size:18px;color:#f0f0f0}
.hero-title{left:220px;top:205px;font-family:"Montserrat",sans-serif;font-weight:700;font-size:31px;color:#fff}
.hero-copy{left:224px;top:245px;width:350px;font-size:8.5px;line-height:13px;color:#f5f5f5;font-weight:700}
.btn-primary{left:224px;top:300px;width:123px;height:32px;border-radius:2px;
  background:linear-gradient(#4fe06a,var(--green-dark));color:#0f2a14;font-family:"Montserrat",sans-serif;
  font-size:13px;font-weight:600;display:flex;align-items:center;justify-content:center;letter-spacing:.3px}
.slider-dots{left:223px;top:414px;display:flex;gap:3px;align-items:center}
.slider-dots i{display:block;width:8px;height:8px;border-radius:50%;background:#111}
.slider-dots i.on{width:22px;border-radius:4px;background:var(--green)}

/* welcome */
.welcome{position:absolute;left:0;top:448px;width:970px;height:163px;background:var(--band)}
.welcome-kicker{left:190px;top:470px;font-family:"Montserrat",sans-serif;font-weight:300;font-size:19px;color:#eee}
.welcome-title{left:190px;top:488px;font-family:"Montserrat",sans-serif;font-weight:600;font-size:32px;color:#fff}
.welcome-rule{left:190px;top:530px;width:325px;height:1px;background:var(--rule)}
.welcome-copy{left:190px;top:544px;width:330px;font-size:8.5px;line-height:12.5px;color:#e0e0e0;font-weight:700}
.callout-text{left:557px;top:523px;width:192px;text-align:center;font-size:8px;color:#fff;font-weight:700}

/* services */
.services-head{position:absolute;left:0;top:611px;width:970px;height:97px;background:var(--band-alt);
  border-top:1px solid #2a2a2a;border-bottom:1px solid #2a2a2a}
.section-title{left:0;top:630px;width:970px;text-align:center;font-family:"Montserrat",sans-serif;
  font-size:24px;color:#fff;font-weight:300;letter-spacing:.5px}
.section-title b{font-weight:600}
.title-line{top:645px;height:3px;background:#2e2e2e}
.services-intro{left:370px;top:661px;width:230px;text-align:center;font-size:7.5px;line-height:11px;color:#ccc}
.services-row{position:absolute;left:0;top:708px;width:970px;height:163px;background:var(--band)}
.service{position:absolute;top:722px;width:130px;text-align:center}
.service h3{font-family:"Lato",sans-serif;font-weight:400;font-size:11px;color:var(--green);margin-bottom:6px}
.service svg{display:block;margin:0 auto 6px}
.service p{font-size:7.5px;line-height:11px;color:#ddd}
.btn-small{position:absolute;width:61px;height:17px;background:#050505;color:var(--green);
  font-size:7px;display:flex;align-items:center;padding-left:6px}
.btn-small::after{content:"→";position:absolute;right:8px;color:#fff;font-size:8px}
.pager{width:22px;height:22px;border-radius:50%;background:#2f2f2f;border:1px solid #444;
  display:flex;align-items:center;justify-content:center;color:#aaa;font-size:10px}

/* about / works */
.about-works{position:absolute;left:0;top:871px;width:970px;height:260px;background:var(--band-deep)}
.block-kicker{font-family:"Montserrat",sans-serif;font-weight:300;font-size:16px;color:#eee}
.block-title{font-family:"Montserrat",sans-serif;font-weight:600;font-size:20px;color:#fff}
.block-rule{height:1px;background:var(--rule)}
.about-copy{left:189px;top:944px;width:315px;font-size:7.3px;line-height:10.2px;color:#ddd}
.about-copy p+p{margin-top:10px}
.work-thumb{position:absolute;width:106px;height:57px;border:1px solid #555}

/* footer */
.site-footer{position:absolute;left:0;top:1131px;width:970px;height:69px;background:var(--footer)}
.footer-nav a{position:absolute;top:1159px;font-family:"Montserrat",sans-serif;font-size:7.5px;font-weight:600;color:#eee;text-decoration:none}
.footer-nav a.current{color:var(--green)}
.footer-nav span{position:absolute;top:1157px;color:#ddd;font-size:9px}
.footer-divider{left:563px;top:1131px;width:1px;height:69px;background:#2a2a2a}
.footer-mark{left:581px;top:1147px;width:36px;height:36px;border-radius:50%;background:#2b2b2b}
.footer-legal{left:626px;top:1144px;font-size:7px;color:#8a8a8a;font-family:"Montserrat",sans-serif}
.footer-touch{left:628px;top:1164px;font-size:7px;color:#8a8a8a;font-family:"Montserrat",sans-serif}
.social{width:18px;height:18px;border-radius:50%;background:#4a4a4a;top:1159px}
</style>
</head>
<body>

<header class="site-header">
  <div class="brand"><span class="brand-dot"></span>Orvik Lines</div>
  <div class="nav-active-bar"></div>
  <svg class="abs" style="left:442px;top:26px" width="20" height="16" viewBox="0 0 20 16" aria-label="Home">
    <path d="M10 1 L19 8 H16 V15 H12 V10 H8 V15 H4 V8 H1 Z" fill="#9a9a9a"/>
  </svg>
  <nav class="main-nav">
    <a href="#" style="left:496px">ABOUT</a>
    <a href="#" style="left:562px">SERVICES</a>
    <a href="#" style="left:643px">WORKS</a>
    <a href="#" style="left:711px">CONTACT US</a>
  </nav>
</header>

<section>
  <div class="hero-media" role="img" aria-label="Black and white photo of a rope access technician cleaning the glass facade of a tall building"></div>
  <div class="abs hero-lead">Lorem Ipsum is simply dummy text and</div>
  <h1 class="abs hero-title">typesetting industry.</h1>
  <p class="abs hero-copy">Lorem ipsum dolor sit amet, consectetur adipiscing elit. Aliquam sit amet ipsum lacus. Cras enim urna, aliquam sed molestie eget, ornare id nisl. Donec sed malesuada diam. Morbi dictum ullamcorper mi. Suspendisse nec lacus nec velit sodales</p>
  <a class="abs btn-primary">READ MORE</a>
  <div class="abs slider-dots"><i class="on"></i><i></i><i></i></div>
</section>

<section class="welcome"></section>
<div class="abs welcome-kicker">welcome to</div>
<h2 class="abs welcome-title">Orvik Lines</h2>
<div class="abs welcome-rule"></div>
<p class="abs welcome-copy">Lorem ipsum dolor sit amet, consectetur adipiscing elit. Aliquam sit amet ipsum lacus. Cras enim urna, aliquam sed molestie eget, ornare id nisl. Donec sed malesuada diam. Morbi dictum ullamcorper mi. Suspendisse nec lacus nec velit sodales</p>
<svg class="abs" style="left:552px;top:510px" width="204" height="56" viewBox="0 0 204 56">
  <ellipse cx="101" cy="20" rx="96" ry="14" fill="none" stroke="#e8e8e8" stroke-width="1.2"/>
  <path d="M26 31 C20 38 22 45 20 52" fill="none" stroke="#ccc" stroke-width="1"/>
  <path d="M16 47 L20 53 L25 48" fill="none" stroke="#ccc" stroke-width="1"/>
</svg>
<div class="abs callout-text">check our services below we are expertise in</div>

<section class="services-head"></section>
<div class="abs title-line" style="left:187px;width:174px"></div>
<div class="abs title-line" style="left:608px;width:159px"></div>
<h2 class="abs section-title">OUR <b>SERVICES</b></h2>
<p class="abs services-intro">Lorem ipsum dolor sit amet, consectetur adipiscing elit. Aliquam sit amet ipsum lacus. Cras enim urna, aliquam sed molestie eget, ornare id nisl.</p>

<section class="services-row"></section>
<svg class="abs" style="left:237px;top:695px" width="26" height="14" viewBox="0 0 26 14"><path d="M0 14 L13 1 L26 14 Z" fill="#2b2b2b"/></svg>

<div class="abs pager" style="left:142px;top:775px">‹</div>
<div class="abs pager" style="left:800px;top:775px">›</div>

<div class="service" style="left:184px">
  <h3>Rope Access</h3>
  <svg width="26" height="28" viewBox="0 0 26 28" aria-label="Rope icon"><line x1="13" y1="0" x2="13" y2="14" stroke="var(--green)" stroke-width="2"/><circle cx="13" cy="19" r="6" fill="none" stroke="var(--green)" stroke-width="3"/></svg>
  <p>Lorem ipsum dolor sit amet, consectetur adipiscing elit. Aliquam sit amet ipsum lacus. Cras enim urna, aliquam sed molestie eget, ornare id nisl.</p>
</div>
<div class="service" style="left:354px">
  <h3>Work at Height</h3>
  <svg width="26" height="28" viewBox="0 0 26 28" aria-label="Ladder icon"><path d="M8 28 L14 0 M16 28 L22 2" stroke="var(--green)" stroke-width="2"/><path d="M9 22 H17 M10.5 15 H18.5 M12 8 H20" stroke="var(--green)" stroke-width="2"/></svg>
  <p>Lorem ipsum dolor sit amet, consectetur adipiscing elit. Aliquam sit amet ipsum lacus. Cras enim urna, aliquam sed molestie eget, ornare id nisl.</p>
</div>
<div class="service" style="left:504px">
  <h3>Windows Cleaning</h3>
  <svg width="26" height="28" viewBox="0 0 26 28" aria-label="Window icon"><rect x="2" y="3" width="22" height="22" fill="none" stroke="var(--green)" stroke-width="2.5"/><path d="M13 3 V25 M2 14 H24" stroke="var(--green)" stroke-width="2"/></svg>
  <p>Lorem ipsum dolor sit amet, consectetur adipiscing elit. Aliquam sit amet ipsum lacus. Cras enim urna, aliquam sed molestie eget, ornare id nisl.</p>
</div>
<div class="service" style="left:655px">
  <h3>Water leak into buildings</h3>
  <svg width="26" height="28" viewBox="0 0 26 28" aria-label="Water drop icon"><path d="M13 3 C18 11 21 15 21 19 A8 8 0 0 1 5 19 C5 15 8 11 13 3 Z" fill="var(--green)"/></svg>
  <p>Lorem ipsum dolor sit amet, consectetur adipiscing elit. Aliquam sit amet ipsum lacus. Cras enim urna, aliquam sed molestie eget, ornare id nisl.</p>
</div>

<a class="btn-small" style="left:208px;top:828px">read more</a>
<a class="btn-small" style="left:391px;top:828px">read more</a>
<a class="btn-small" style="left:536px;top:828px">read more</a>
<a class="btn-small" style="left:690px;top:828px">read more</a>

<section class="about-works"></section>
<div class="abs block-kicker" style="left:188px;top:898px">who</div>
<h2 class="abs block-title" style="left:188px;top:911px">we are</h2>
<div class="abs block-rule" style="left:265px;top:926px;width:238px"></div>
<div class="abs about-copy">
  <p>Lorem ipsum dolor sit amet, consectetur adipiscing elit. Aliquam sit amet ipsum lacus. Cras enim urna, aliquam sed molestie eget, ornare id nisl. Donec sed malesuada diam. Morbi dictum ullamcorper mi. Suspendisse nec lacus nec velit sodales viverra varius in odio. Morbi a gravida risus. Sed metus risus, vestibulum et semper ac, consequat eu massa.</p>
  <p>Cras leo lectus, sollicitudin in suscipit vel, lobortis sit amet dui. Nulla quis diam nec ante iaculis scelerisque et at tellus. Sed vestibulum viverra justo, non varius magna euismod in. Aenean aliquam eros et dui vestibulum vehicula sit amet eu neque. Sed ac velit est, quis commodo nibh. In non enim sem. Morbi sollicitudin pretium nulla non pulvinar. Maecenas ultricies faucibus magna, eu suscipit libero imperdiet quis. Vestibulum ante ipsum primis in faucibus orci luctus et ultrices posuere cubilia Curae; In tempus vestibulum tincidunt. Mauris at placerat massa. Duis faucibus tincidunt nulla, vel malesuada diam viverra sit amet. Cras rutrum velit id elit sodales a sodales elit auctor.</p>
</div>
<a class="btn-small" style="left:189px;top:1086px">read more</a>

<div class="abs block-kicker" style="left:548px;top:898px">our</div>
<h2 class="abs block-title" style="left:548px;top:911px">works</h2>
<div class="abs block-rule" style="left:622px;top:926px;width:95px"></div>
<a class="btn-small" style="left:717px;top:915px">view all</a>
<div class="work-thumb" style="left:548px;top:954px;background:linear-gradient(#8a8f96,#6b5a44)" role="img" aria-label="Photo of a rooftop at sunset during a job"></div>
<div class="work-thumb" style="left:672px;top:954px;background:linear-gradient(#3d5560,#1e2a30)" role="img" aria-label="Photo of a glass facade being serviced"></div>
<div class="work-thumb" style="left:548px;top:1024px;background:linear-gradient(#9a9a9a,#3a3a3a)" role="img" aria-label="Photo of a technician working on a wall"></div>
<div class="work-thumb" style="left:672px;top:1024px;background:linear-gradient(#d6dde3,#8f9aa3)" role="img" aria-label="Photo of window cleaning on a curved glass building"></div>

<footer class="site-footer"></footer>
<nav class="footer-nav">
  <a href="#" class="current" style="left:202px">HOME</a><span style="left:247px">|</span>
  <a href="#" style="left:270px">ABOUT</a><span style="left:319px">|</span>
  <a href="#" style="left:342px">SERVICES</a><span style="left:397px">|</span>
  <a href="#" style="left:422px">WORKS</a><span style="left:473px">|</span>
  <a href="#" style="left:497px">CONTACT US</a>
</nav>
<div class="abs footer-divider"></div>
<div class="abs footer-mark"></div>
<div class="abs footer-legal">Orvik Lines © 2013 &nbsp;|&nbsp; PRIVACY POLICY</div>
<div class="abs footer-touch">GET IN TOUCH</div>
<div class="abs social" style="left:682px" aria-label="frindlo"></div>
<div class="abs social" style="left:702px" aria-label="Social profile"></div>

</body>
</html>
```